insert for clam shell / vape cartridge

Brand : Brevor (roman god of fire)
card insert dimensions are 2.5" in width and 3.375" in height
this is a cannabis product. Open to any and all designs. Currently using very generic text. 5/8" on left edge of design will be covered by the cartridge

Target Market(s)

medical cannabis patients

Industry/Entity Type

Product

Logo Text

Brevor

Requirements
Must have
• logo
Nice to have
• "distilled cannabis oil"
• "no pg/vg"
• subtle use of cannabis leaf
Should not have
• no big (prominent) Pot leaves

```html
<!DOCTYPE html>
<html lang="en">
<head>
<meta charset="utf-8">
<title>Brevor – Cartridge Card Insert</title>
<link rel="stylesheet" href="https://fonts.googleapis.com/css2?family=Quicksand:wght@400;500&family=Marcellus&display=swap">
<style>
  :root {
    --page-bg: #ecebe8;
    --card-bg: #ffffff;
    --card-edge: #1f1f1f;
    --brand-orange: #e85a36;
    --name-orange: #ee8a2c;
    --pattern-light: #f7c48f;
    --pattern-deep: #ef9346;
    --caption-grey: #8c8c8c;
  }
  html, body {
    margin: 0;
    padding: 0;
    width: 1200px;
    height: 1000px;
    overflow: hidden;
    background: var(--page-bg);
  }
  .canvas {
    position: relative;
    width: 1200px;
    height: 1000px;
  }
  .insert-card {
    position: absolute;
    left: 350px;
    top: 163px;
    width: 530px;
    height: 715px;
    box-sizing: border-box;
    background: var(--card-bg);
    border: 2px solid var(--card-edge);
    border-radius: 22px;
    overflow: hidden;
  }
  .pattern-block {
    position: absolute;
    left: 368px;
    width: 130px;
    background: linear-gradient(160deg, var(--pattern-light), var(--pattern-deep));
  }
  .pattern-top    { top: 0;     height: 54px; }
  .pattern-upper  { top: 153px; height: 94px; }
  .pattern-middle { top: 327px; height: 227px; }
  .pattern-bottom { top: 657px; height: 58px; }

  .brand-name {
    position: absolute;
    right: 32px;
    top: 38px;
    margin: 0;
    font-family: "Quicksand", sans-serif;
    font-weight: 500;
    font-size: 96px;
    line-height: 1;
    color: var(--brand-orange);
    letter-spacing: 1px;
  }
  .product-type {
    position: absolute;
    right: 33px;
    top: 260px;
    margin: 0;
    width: 220px;
    text-align: right;
    font-family: "Marcellus", serif;
    font-size: 22px;
    line-height: 32px;
    color: var(--brand-orange);
  }
  .strain-name {
    position: absolute;
    right: 32px;
    top: 565px;
    margin: 0;
    font-family: "Quicksand", sans-serif;
    font-weight: 400;
    font-size: 44px;
    line-height: 1;
    color: var(--name-orange);
  }
  .carrier-note {
    position: absolute;
    right: 33px;
    top: 624px;
    margin: 0;
    font-family: "Marcellus", serif;
    font-size: 18px;
    color: var(--caption-grey);
  }
</style>
</head>
<body>
<div class="canvas">
  <div class="insert-card">
    <div class="pattern-block pattern-top" role="img" aria-label="Decorative orange ring and checker pattern"></div>
    <h1 class="brand-name">Brevor</h1>
    <div class="pattern-block pattern-upper" role="img" aria-label="Decorative orange ring and checker pattern"></div>
    <p class="product-type">distilled cannabis<br>oil</p>
    <div class="pattern-block pattern-middle" role="img" aria-label="Decorative orange ring and checker pattern"></div>
    <p class="strain-name">Citrus Spark</p>
    <p class="carrier-note">no pg/vg</p>
    <div class="pattern-block pattern-bottom" role="img" aria-label="Decorative orange ring and checker pattern"></div>
  </div>
</div>
</body>
</html>
```